Smile club flyer design

I am launching an office smile club and would like a design that sits my branding and that is appealing to customers. I have a design (I need a new one) that has all the information.
My website is maplecrestdentalcarewv.com
Brand color is green. The design can be any color

Target Market(s)

Ages 30+

Industry/Entity Type

Dental

Font styles to use
Serif

Requirements
Must have
• Appealing to patients

```html
<!DOCTYPE html>
<html lang="en">
<head>
<meta charset="utf-8">
<title>Maplecrest Dental Care – Smile Club Membership</title>
<link rel="stylesheet" href="https://fonts.googleapis.com/css2?family=Libre+Baskerville:wght@700&family=Montserrat:wght@300;400;500;700;800;900&family=Nunito:wght@800;900&display=swap">
<style>
  :root {
    --page-bg: #ececec;
    --mint: #ddeed6;
    --deep-teal: #156b60;
    --bright-teal: #10b5a4;
    --pill-teal: #1a9e94;
    --brand-green: #0e8a3e;
    --card-green: #0e9444;
    --olive: #a38731;
    --lime: #8cc63f;
    --title-mint: #cfeeb0;
    --ink: #1f2a26;
    --white: #ffffff;
    --silver-light: #e4e6e7;
    --silver-dark: #8e9396;
  }
  * { box-sizing: border-box; margin: 0; padding: 0; }
  html, body { width: 1200px; height: 1200px; overflow: hidden; }
  body {
    background: var(--page-bg);
    font-family: "Montserrat", sans-serif;
    color: var(--ink);
    position: relative;
  }
  .flyer {
    position: absolute; left: 250px; top: 75px;
    width: 700px; height: 1050px;
    background: var(--mint);
    overflow: hidden;
  }
  .flyer__top { position: absolute; left: 0; top: 0; width: 700px; height: 140px; background: var(--white); }
  .flyer__band { position: absolute; left: 0; top: 0; width: 700px; height: 330px; }

  .brand { position: absolute; left: 0; top: 20px; width: 700px; text-align: center; z-index: 3; }
  .brand__name {
    font-family: "Libre Baskerville", serif; font-weight: 700;
    font-size: 38px; color: var(--brand-green); line-height: 1; letter-spacing: -0.5px;
  }
  .brand__sub {
    font-family: "Libre Baskerville", serif; font-weight: 700;
    font-size: 15px; color: var(--brand-green); letter-spacing: 5px; margin-top: 8px;
  }

  .instrument {
    position: absolute; border-radius: 14px; z-index: 2;
    background: linear-gradient(90deg, var(--silver-dark), var(--silver-light) 45%, var(--silver-dark));
  }
  .instrument--pick { left: 88px; top: 0; width: 34px; height: 190px; }
  .instrument--mirror { left: 498px; top: 105px; width: 200px; height: 40px; transform: rotate(28deg); transform-origin: left center; }
  .instrument--handpiece { left: 0; top: 300px; width: 170px; height: 60px; transform: rotate(-8deg); }
  .instrument--probe { left: 535px; top: 335px; width: 165px; height: 26px; }

  .headline { position: absolute; left: 0; width: 700px; text-align: center; color: var(--white); z-index: 3; }
  .headline--intro { top: 146px; font-weight: 300; font-size: 28px; letter-spacing: 4px; }
  .headline--club { top: 180px; font-weight: 900; font-size: 67px; letter-spacing: -1px; line-height: 1; }
  .headline--member { top: 252px; font-weight: 800; font-size: 34px; letter-spacing: 4.5px; }

  .tagline { position: absolute; left: 0; width: 700px; text-align: center; z-index: 3; }
  .tagline--lead { top: 334px; font-size: 21px; font-weight: 400; letter-spacing: 1.8px; color: var(--brand-green); }
  .tagline--strong { top: 363px; font-family: "Nunito", sans-serif; font-size: 21px; font-weight: 900; letter-spacing: 1.2px; color: var(--deep-teal); }

  .plan {
    position: absolute; width: 207px;
    background: var(--white); border-radius: 19px; overflow: hidden;
  }
  .plan--core { left: 30px; top: 410px; height: 320px; }
  .plan--bright { left: 247px; top: 410px; height: 320px; }
  .plan--total { left: 463px; top: 410px; height: 320px; }
  .plan--refresh { left: 30px; top: 742px; height: 270px; }
  .plan__art { position: absolute; left: 0; top: 0; width: 207px; height: 150px; }
  .plan__title {
    position: absolute; left: 0; top: 12px; width: 100%; text-align: center;
    font-family: "Nunito", sans-serif; font-weight: 900; font-size: 25px; color: var(--title-mint); line-height: 1;
  }
  .plan__type {
    position: absolute; left: 0; top: 43px; width: 100%; text-align: center;
    font-size: 16px; font-weight: 400; color: var(--white); line-height: 1;
  }
  .plan__price {
    position: absolute; left: 0; top: 82px; width: 100%; text-align: center;
    color: var(--white); line-height: 1; white-space: nowrap;
  }
  .plan__amount { font-family: "Nunito", sans-serif; font-weight: 900; font-size: 35px; }
  .plan__period { font-weight: 300; font-size: 21px; }
  .plan__tag {
    position: absolute; left: 0; top: 0; width: 62px; height: 30px;
    background: var(--deep-teal); border-bottom-right-radius: 26px;
    color: var(--white); font-weight: 700; font-size: 13px; letter-spacing: 0.5px;
    padding: 10px 0 0 12px; line-height: 1; z-index: 2;
  }
  .plan__list { position: absolute; left: 12px; top: 153px; right: 8px; list-style: none; }
  .plan__item {
    position: relative; padding-left: 17px;
    font-size: 13px; font-weight: 500; line-height: 16.5px; margin-bottom: 16.5px;
  }
  .plan__item svg { position: absolute; left: 0; top: 3px; width: 12px; height: 12px; }

  .finance { position: absolute; left: 271px; width: 396px; text-align: center; }
  .finance__label { top: 761px; font-size: 12px; font-weight: 500; letter-spacing: 0.6px; }
  .finance__note { top: 835px; font-size: 12px; font-weight: 500; letter-spacing: 0.6px; }
  .partners { position: absolute; left: 271px; top: 787px; width: 396px; height: 34px; }
  .partner {
    position: absolute; top: 2px; font-weight: 700; font-size: 24px; color: var(--deep-teal); line-height: 30px;
  }
  .partner--one { left: 16px; }
  .partner--two { left: 246px; }
  .partners__divider { position: absolute; left: 211px; top: 0; width: 1.5px; height: 34px; background: var(--deep-teal); }

  .fee-pill {
    position: absolute; left: 322px; top: 874px; width: 283px; height: 25px;
    background: var(--pill-teal); border-radius: 13px;
    color: var(--white); font-size: 10.5px; font-weight: 500; text-align: center; line-height: 25px;
  }
  .cta {
    position: absolute; left: 271px; top: 918px; width: 396px; height: 140px;
    background: var(--card-green); border-radius: 38px 38px 0 0; text-align: center; color: var(--white);
  }
  .cta__lead { margin-top: 23px; font-size: 21px; font-weight: 400; letter-spacing: 1.2px; line-height: 1; }
  .cta__phone { margin-top: 8px; font-weight: 800; font-size: 45px; letter-spacing: 1px; line-height: 1; }
</style>
</head>
<body>
<main class="flyer">
  <div class="flyer__top"></div>
  <svg class="flyer__band" viewBox="0 0 700 330" aria-hidden="true">
    <path d="M0,69 Q350,152 700,79 V260 Q350,372 0,260 Z" fill="var(--bright-teal)"/>
    <path d="M0,77 Q350,164 700,87 V260 Q350,372 0,260 Z" fill="var(--deep-teal)"/>
  </svg>

  <div class="instrument instrument--pick" role="img" aria-label="Illustration of a dental explorer pick"></div>
  <div class="instrument instrument--mirror" role="img" aria-label="Illustration of a dental mouth mirror"></div>
  <div class="instrument instrument--handpiece" role="img" aria-label="Illustration of a dental handpiece drill"></div>
  <div class="instrument instrument--probe" role="img" aria-label="Illustration of a dental probe"></div>

  <header class="brand">
    <div class="brand__name">Maplecrest</div>
    <div class="brand__sub">DENTAL CARE</div>
  </header>

  <div class="headline headline--intro">INTRODUCING</div>
  <h1 class="headline headline--club">SMILE CLUB</h1>
  <div class="headline headline--member">MEMBERSHIP</div>

  <p class="tagline tagline--lead">AFFORDABLE DENTAL CARE</p>
  <p class="tagline tagline--strong">NO INSURANCE REQUIRED</p>

  <svg width="0" height="0" style="position:absolute">
    <defs>
      <symbol id="tick" viewBox="0 0 12 12">
        <circle cx="6" cy="6.3" r="4.9" fill="none" stroke="var(--card-green)" stroke-width="1.4"/>
        <path d="M3.6,6.1 L5.6,8.1 L10.6,1.6" fill="none" stroke="var(--olive)" stroke-width="1.6" stroke-linecap="round" stroke-linejoin="round"/>
      </symbol>
      <symbol id="plan-art" viewBox="0 0 207 150">
        <path d="M0,0 H207 V146 Q103.5,100 0,146 Z" fill="var(--olive)"/>
        <path d="M0,0 H207 V58 Q103.5,104 0,58 Z" fill="var(--lime)"/>
        <path d="M0,0 H207 V55 Q103.5,91 0,55 Z" fill="var(--card-green)"/>
      </symbol>
    </defs>
  </svg>

  <section class="plan plan--core">
    <svg class="plan__art" aria-hidden="true"><use href="#plan-art"/></svg>
    <h2 class="plan__title">Core Care</h2>
    <div class="plan__type">Preventive</div>
    <div class="plan__price"><span class="plan__amount">$39</span><span class="plan__period">/month</span></div>
    <ul class="plan__list">
      <li class="plan__item"><svg><use href="#tick"/></svg>Comprehensive Annual Exam</li>
      <li class="plan__item"><svg><use href="#tick"/></svg>2 Professional Cleanings per Year</li>
      <li class="plan__item"><svg><use href="#tick"/></svg>Routine Bitewing X-rays</li>
      <li class="plan__item"><svg><use href="#tick"/></svg>10% Saving on Treatment</li>
    </ul>
  </section>

  <section class="plan plan--bright">
    <svg class="plan__art" aria-hidden="true"><use href="#plan-art"/></svg>
    <h2 class="plan__title">Bright</h2>
    <div class="plan__type">Cosmetic</div>
    <div class="plan__price"><span class="plan__amount">$59</span><span class="plan__period">/month</span></div>
    <ul class="plan__list">
      <li class="plan__item"><svg><use href="#tick"/></svg>Annual In-Office<br>Whitening<br>(Top &amp; Bottom)</li>
      <li class="plan__item"><svg><use href="#tick"/></svg>Custom Whitenign Trays</li>
      <li class="plan__item"><svg><use href="#tick"/></svg>15% Savings on Elective Treatment</li>
    </ul>
  </section>

  <section class="plan plan--total">
    <svg class="plan__art" aria-hidden="true"><use href="#plan-art"/></svg>
    <h2 class="plan__title">Total Smile</h2>
    <div class="plan__type">Periodontal</div>
    <div class="plan__price"><span class="plan__amount">$89</span><span class="plan__period">/month</span></div>
    <ul class="plan__list">
      <li class="plan__item"><svg><use href="#tick"/></svg>3-4 Perio Maintenance Visits per Year</li>
      <li class="plan__item"><svg><use href="#tick"/></svg>1 Comprehensive Exam</li>
      <li class="plan__item"><svg><use href="#tick"/></svg>Diagnostic X-rays</li>
      <li class="plan__item"><svg><use href="#tick"/></svg>15% Savings on Restorative &amp; Elective Care</li>
    </ul>
  </section>

  <section class="plan plan--refresh">
    <svg class="plan__art" aria-hidden="true"><use href="#plan-art"/></svg>
    <div class="plan__tag">NEW</div>
    <h2 class="plan__title">Smile</h2>
    <div class="plan__type">Refresh Package</div>
    <div class="plan__price"><span class="plan__amount">$499</span></div>
    <ul class="plan__list">
      <li class="plan__item"><svg><use href="#tick"/></svg>Cleaning +<br>Comprehensive Exam + Whitening</li>
      <li class="plan__item"><svg><use href="#tick"/></svg>Limited Time Offer</li>
    </ul>
  </section>

  <p class="finance finance__label">FLEXIBLE FICANCING FOR TREATMENT:</p>
  <div class="partners">
    <span class="partner partner--one">MediSpread</span>
    <span class="partners__divider"></span>
    <span class="partner partner--two">Plumline</span>
  </div>
  <p class="finance finance__note">PAYMENT PLANS AVAILABLE</p>

  <div class="fee-pill">*$49 Lifetime Activation Fee (Non-Refundable)</div>

  <section class="cta">
    <p class="cta__lead">JOIN SMILE CLUB TODAY!</p>
    <p class="cta__phone">0865-555-014</p>
  </section>
</main>
</body>
</html>
```